Creative Businesss Card desgin!

Create a business card for our business Gleam window cleaning!
We are open to creative ideas as long as it maintains a professional image.

Target Market(s)

Small Commercial window cleaning clients including car dealerships, strata manager, cafe

Industry/Entity Type

Window Cleaning

Contact Information for Business Card

Daniel Prescott
General Manager
Gleam Window Cleaning

daniel@gleamservices.com.au
pane-care-southbank.com.au
Ph: 1800 GET GLEAM
Mob: 0437 582 061

Colors
fbed22
0392cd

Requirements
Should not have
• Stock window cleaning/ squeegee graphics

```html
<!DOCTYPE html>
<html lang="en">
<head>
<meta charset="utf-8">
<title>Gleam Window Cleaning – Business Card</title>
<link href="https://fonts.googleapis.com/css2?family=Arimo:wght@400;700&display=swap" rel="stylesheet">
<style>
  :root {
    --navy: #0b2a80;
    --yellow: #fde400;
    --white: #ffffff;
    --mist: #d6ebf6;
    --page: #ffffff;
    --edge: #2a2a30;
  }
  * { box-sizing: border-box; margin: 0; padding: 0; }
  html, body {
    width: 1200px;
    height: 798px;
    overflow: hidden;
    background: var(--page);
    font-family: "Arimo", Arial, sans-serif;
  }
  .canvas {
    position: relative;
    width: 1200px;
    height: 798px;
  }
  .card {
    position: absolute;
    width: 520px;
    height: 318px;
    overflow: hidden;
    box-shadow: 0 6px 0 var(--edge), 0 10px 18px rgba(0,0,0,0.18);
  }

  /* Front: contact side */
  .card-front {
    left: 70px;
    top: 120px;
    background: var(--white);
  }
  .front-texture {
    position: absolute;
    inset: 0;
    background: radial-gradient(ellipse at 100% 0%, var(--mist) 0%, rgba(214,235,246,0.5) 40%, rgba(255,255,255,0) 75%);
  }
  .brand-panel {
    position: absolute;
    left: 0;
    top: 0;
    width: 260px;
    height: 100%;
  }
  .brand-panel svg { display: block; width: 100%; height: 100%; }
  .brand-mark {
    position: absolute;
    left: 22px;
    top: 22px;
    color: var(--yellow);
    font-weight: 700;
    line-height: 1;
  }
  .brand-mark .brand-name { display: block; font-size: 30px; letter-spacing: 1px; }
  .brand-mark .brand-sub { display: block; font-size: 9.5px; letter-spacing: 0.6px; margin-top: 4px; }

  .contact {
    position: absolute;
    right: 26px;
    top: 30px;
    text-align: right;
    color: var(--navy);
    font-weight: 700;
  }
  .contact-name { font-size: 27px; }
  .contact-role { font-size: 18px; margin-top: 6px; }
  .contact-phones { margin-top: 30px; font-size: 16.5px; line-height: 1.45; }
  .contact-online { margin-top: 30px; font-size: 15.5px; line-height: 1.45; }

  /* Back: brand side */
  .card-back {
    left: 620px;
    top: 360px;
    background: var(--yellow);
  }
  .back-lockup {
    position: absolute;
    left: 50%;
    top: 50%;
    transform: translate(-50%, -50%) rotate(-33deg);
    color: var(--navy);
    font-weight: 700;
    text-align: center;
    line-height: 1;
    white-space: nowrap;
  }
  .back-lockup .brand-name { display: block; font-size: 132px; letter-spacing: 4px; }
  .back-lockup .brand-sub { display: block; font-size: 44px; letter-spacing: 2px; margin-top: 6px; }
</style>
</head>
<body>
  <main class="canvas">
    <section class="card card-front" aria-label="Business card, contact side">
      <div class="front-texture" role="img" aria-label="Soft light blue dotted texture"></div>
      <div class="brand-panel">
        <svg viewBox="0 0 260 318" preserveAspectRatio="none" aria-hidden="true">
          <polygon points="0,0 230,0 160,318 0,318" fill="var(--navy)"/>
          <polygon points="230,0 244,0 174,318 160,318" fill="var(--yellow)"/>
        </svg>
      </div>
      <div class="brand-mark">
        <span class="brand-name">GLEAM</span>
        <span class="brand-sub">WINDOW CLEANING</span>
      </div>
      <div class="contact">
        <p class="contact-name">Daniel Prescott</p>
        <p class="contact-role">General Manager</p>
        <div class="contact-phones">
          <p>Ph: 1800 GET GLEAM</p>
          <p>Mob: 0437 582 061</p>
        </div>
        <div class="contact-online">
          <p>daniel@gleamservices.com.au</p>
          <p>pane-care-southbank.com.au</p>
        </div>
      </div>
    </section>

    <section class="card card-back" aria-label="Business card, brand side">
      <div class="back-lockup">
        <span class="brand-name">GLEAM</span>
        <span class="brand-sub">WINDOW CLEANING</span>
      </div>
    </section>
  </main>
</body>
</html>
```